"The Lamplighter's Ledger" book cover

Book cover for both print paperback and ebook versions of the book.
The book consists of a series of short stories (chapters) depicting various unusual stories of clients of the astrologer and personal experience of the author, a person with a professional duty to forecast future.

It should be neutral to positive. There is no restriction regarding the colors – it can be both B&W and full color.
The design should be original and not include any images which require obtaining a copyright license to use. Symbols in common use and not copyrighted are probably ok. The designer should use appropriate symbols attached in the word file.
Text for the back cover is not yet available, will be ready by the end of the project. The photos of the author for the backside are attached, please choose which you consider the best.
I will need PDF, JPEG, TIFF (all formats both in CMYK and RGB) and the source file. For CMYK, we need files with no color profiles assigned.

Target Market(s)

General

Colors

Designer to choose colors to be used in the design.

Requirements
Must have
• Please the project description
Nice to have
Should not have
• Stock images or anything else requiring additional copyright discussions and negotiations.

```html
<!DOCTYPE html>
<html lang="en">
<head>
<meta charset="utf-8">
<title>The Lamplighter's Ledger — Cover</title>
<link rel="stylesheet" href="https://fonts.googleapis.com/css2?family=Anton&family=Oswald:wght@300;400;600;700&display=swap">
<style>
  :root {
    --teal: #0a8ab0;
    --navy: #0d1f5c;
    --sky: #16aee8;
    --ink: #1a1a1a;
    --block: #0066b3;
    --paper: #ffffff;
    --chart: #eef1f4;
  }
  * { margin: 0; padding: 0; box-sizing: border-box; }
  html, body { width: 1200px; height: 902px; overflow: hidden; background: var(--paper); }
  .cover { position: relative; width: 1200px; height: 902px; overflow: hidden;
    background: var(--paper); font-family: 'Oswald', sans-serif; color: var(--ink); }
  .chart-backdrop { position: absolute; inset: 0;
    background: radial-gradient(circle at 760px 300px, rgba(230,234,238,0.9) 0, rgba(240,243,246,0.6) 360px, rgba(255,255,255,0) 620px); }

  /* back cover */
  .back-title { position: absolute; left: 40px; width: 508px; top: 34px; text-align: center;
    font-family: 'Anton', sans-serif; font-size: 40px; line-height: 56px; color: var(--teal); letter-spacing: 0.5px; }
  .back-rule { position: absolute; left: 80px; top: 97px; width: 416px; height: 2px; background: var(--block); }
  .back-subtitle { position: absolute; left: 40px; width: 508px; top: 112px; text-align: center;
    font-weight: 700; font-size: 18px; color: var(--navy); }
  .blurb { position: absolute; left: 60px; top: 168px; width: 466px; font-weight: 300; font-size: 15.4px;
    line-height: 20.6px; text-align: justify; }
  .blurb p { margin-bottom: 20.6px; }
  .sign-row { position: absolute; left: 112px; top: 542px; width: 370px; display: flex; justify-content: space-between;
    font-size: 13px; color: var(--block); font-family: 'Segoe UI Symbol', 'DejaVu Sans', sans-serif; }
  .author-bio { position: absolute; left: 60px; top: 588px; width: 470px; }
  .author-bio svg { position: absolute; left: 0; top: 0; }
  .author-bio p { position: absolute; left: 104px; top: 0; width: 420px; font-weight: 300; font-size: 15.4px; line-height: 20.6px; }
  .author-bio .bio-line { display: block; padding-left: 13px; }
  .author-bio .bio-last { display: block; }
  .author-bio .name { color: var(--sky); font-weight: 600; font-style: italic; }
  .isbn-block { position: absolute; left: 347px; top: 739px; width: 207px; height: 123px; background: var(--block); }

  /* spine */
  .spine { position: absolute; left: 576px; width: 40px; writing-mode: vertical-rl; display: flex; align-items: center; }
  .spine-title { top: 40px; height: 250px; font-family: 'Anton', sans-serif; font-size: 20px; color: var(--teal); }
  .spine-subtitle { top: 328px; height: 360px; font-weight: 700; font-size: 15px; color: var(--navy); }
  .spine-author { top: 728px; height: 150px; font-weight: 300; font-size: 20px; color: var(--navy); }

  /* front cover */
  .front-author { position: absolute; left: 740px; width: 330px; top: 32px; text-align: center;
    font-weight: 300; font-size: 44px; line-height: 56px; color: var(--navy); letter-spacing: 0.5px; }
  .front-title { position: absolute; left: 649px; top: 110px; font-family: 'Anton', sans-serif;
    font-size: 86px; line-height: 88px; color: var(--teal); }
  .front-subtitle { position: absolute; left: 653px; top: 374px; font-weight: 700; font-size: 22.5px; color: var(--navy); }
  .author-photo { position: absolute; left: 752px; top: 428px; width: 284px; height: 474px; }
  .translator { position: absolute; left: 760px; top: 836px; font-weight: 700; font-size: 25px; color: var(--navy); }
</style>
</head>
<body>
<main class="cover">
  <div class="chart-backdrop" role="img" aria-label="Faint astrological chart wheel with degree markings behind the whole wrap"></div>

  <section class="back-cover">
    <h2 class="back-title">THE LAMPLIGHTER'S LEDGER</h2>
    <div class="back-rule"></div>
    <p class="back-subtitle">Real-life stories on how the stars shape our lives</p>
    <div class="blurb">
      <p>Lorem ipsum dolor sit amet, consectetur adipisicing elit, sed do eiusmod tempor incididunt ut labore et dolore magna aliqua. Ut enim ad minim veniam, quis nostrud exercitation ullamco laboris nisi ut aliquip ex ea commodo consequat.</p>
      <p>Duis aute irure dolor in reprehenderit in voluptate velit esse cillum dolore eu fugiat nulla pariatur. Excepteur sint occaecat cupidatat non proident, sunt in culpa qui officia deserunt mollit anim id est laborum. Sed ut perspiciatis unde omnis iste natus error sit voluptatem accusantium doloremque laudantium, totam rem aperiam, eaque ipsa quae ab illo inventore veritatis et quasi architecto beatae vitae dicta sunt explicabo.</p>
      <p>Nemo enim ipsam voluptatem quia voluptas sit aspernatur aut odit aut fugit, sed quia consequuntur magni dolores eos qui ratione voluptatem sequi nesciunt. Neque porro quisquam est, qui dolorem ipsum quia dolor sit amet, consectetur, adipisci velit, sed quia non numquam eius modi tempora incidunt ut labore et dolore magnam aliquam quaerat voluptatem.</p>
    </div>
    <div class="sign-row" aria-label="Astrological symbols">
      <span>♀</span><span>♆</span><span>♌</span><span>♎</span><span>♏</span><span>♐</span><span>♑</span><span>♒</span><span>♓</span><span>♊</span><span>♂</span><span>♃</span><span>♄</span>
    </div>
    <div class="author-bio">
      <svg width="104" height="110" viewBox="0 0 104 110">
        <path d="M62 108 A54 54 0 1 1 62 2" fill="none" stroke="var(--sky)" stroke-width="5"/>
        <circle cx="58" cy="52" r="49" fill="#e9e6e2" role="img" aria-label="Author portrait"/>
      </svg>
      <p><span class="name">Marina Velskaya</span> Lorem ipsum dolor sit amet, consectetur
        <span class="bio-line">adipisicing elit, sed do eiusmod tempor incididunt ut labore</span>
        <span class="bio-line">et dolore magna aliqua. Ut enim ad minim veniam, quis</span>
        <span class="bio-line">nostrud exercitation ullamco laboris nisi ut aliquip ex</span>
        <span class="bio-last">ea commodo consequat.</span></p>
    </div>
    <div class="isbn-block"></div>
  </section>

  <section class="spine-area">
    <div class="spine spine-title">THE LAMPLIGHTER'S LEDGER</div>
    <div class="spine spine-subtitle">Real-life stories on how the stars shape our lives</div>
    <div class="spine spine-author">MARINA VELSKAYA</div>
  </section>

  <section class="front-cover">
    <p class="front-author">MARINA VELSKAYA</p>
    <h1 class="front-title">THE<br>LAMPLIGHTER'S<br>LEDGER</h1>
    <p class="front-subtitle">Real-life stories on how the stars shape our lives</p>
    <svg class="author-photo" viewBox="0 0 284 474" role="img" aria-label="Photograph of the author in a light sweater, standing and smiling">
      <defs>
        <linearGradient id="photoTone" x1="0" y1="0" x2="0" y2="1">
          <stop offset="0" stop-color="#e8d9b0"/>
          <stop offset="0.35" stop-color="#ece9e6"/>
          <stop offset="1" stop-color="#d6d6d8"/>
        </linearGradient>
      </defs>
      <path d="M90 0 H200 L220 150 Q284 180 284 300 V474 H0 V300 Q0 180 70 150 Z" fill="url(#photoTone)"/>
    </svg>
    <p class="translator">Translated by Helen Ashcombe</p>
  </section>
</main>
</body>
</html>
```